Web Design Project

My website was fine - years ago. But it's way, way overdue for an overhaul. When I started my business almost 20 years ago, I wanted to be edgy. And my website was just that. Color, style, voice. Edgy. Today, my clients are corporations. I'm older, more experienced - but still a little edgy. It's controlled edge. What I want now is sophisticated. Savvy. Corporate but cool. Grown up.

My clients are primarily - but not exclusively - in healthcare. But I don't want a healthcare site. I provide the following services:
1. Writing - white papers, brochures, web pages, speechwriting, etc.
2. Marketing strategy
3. Public relations services
4. Thought leader development
5. Training
I couldn't upload all the icons but I can send them. They correspond with the pages as follows and should be used in the design:

1. Writing- nib.png
2. Marketing strategy-compass.png
3. Public relations services-microphone.png
4. Thought leader development-lightbulb.png
5. Training: cogs-training.png or key.png

I will have a blog, and a portfolio of some kind.

I don't want something that looks like a template.
Updates

Project Deadline Extended
Reason: Just made this a committed payment. I apologize for not doing so from the start. Nobody should work for free.

Project Deadline Extended
Reason: Several folks have asked to resubmit, and it has taken me a while to provide feedback.

Dear Designers,

I am so sorry to have been so slow to select. I've had professional and personal issues to deal with. I am actively trying to select a design, however, and will do so in the next two days. Thanks so much for your patience and hard work.

Marla

Thanks so much to everyone who has submitted a design. I had great luck crowdsourcing my logo, but I'm starting to realize that website design is a totally different animal. All of your designs are great, but they all look exactly like templates. And maybe that's the way it's supposed to be, the way it should be. I don't want to use stock photography. It needs to be more personalized than that. I'm open to illustration or even using my own photo on the site, but stock photography won't work for me. If anyone wants to submit something else - and I understand if you don't - please feel free. 

Target Market(s)

C-suite executives; corporations, larger businesses who need marketing writing

Industry/Entity Type

Healthcare

Requirements
Must have
• Logo (somewhere)
Icons
Nice to have
• Level-specific page design (e.g, Home = Level 1, Tabs = Level 2, etc). I'd like it to have a certain order.

```html
<!DOCTYPE html>
<html lang="en">
<head>
<meta charset="utf-8">
<title>The Crux — Home</title>
<link rel="stylesheet" href="https://fonts.googleapis.com/css2?family=Open+Sans:ital,wght@0,400;0,500;0,600;0,700;1,700&display=swap">
<style>
  :root {
    --purple: #7f2583;
    --purple-deep: #5e1a66;
    --purple-light: #a55aa9;
    --orange: #f7941d;
    --gold: #f5a81c;
    --rule: #555555;
    --white: #ffffff;
  }
  * { margin: 0; padding: 0; box-sizing: border-box; }
  html, body { width: 1200px; height: 1000px; overflow: hidden; background: var(--white); }
  body { font-family: "Open Sans", Arial, sans-serif; position: relative; }

  .member-link {
    position: absolute; top: 5px; right: 52px;
    font-size: 13px; font-weight: 700; color: var(--orange); text-decoration: none;
  }

  .brand { position: absolute; top: 8px; left: 0; width: 1200px; text-align: center; }
  .brand-mark { display: block; width: 69px; height: 69px; margin: 0 auto; background: var(--purple); }
  .brand-name {
    display: block; margin-top: 22px;
    font-size: 44px; font-weight: 500; letter-spacing: 3px; color: var(--purple); line-height: 1;
  }

  .rule { position: absolute; left: 60px; width: 1088px; height: 1px; background: var(--rule); }
  .rule--top { top: 185px; }
  .rule--nav { top: 239px; }
  .rule--foot { top: 913px; }

  .main-nav { position: absolute; top: 198px; left: 0; width: 1200px; }
  .main-nav a {
    position: absolute; font-size: 21px; font-weight: 600; color: var(--orange);
    text-decoration: none; white-space: nowrap;
  }

  .feature-art { position: absolute; top: 0; left: 0; }

  .feature-label { position: absolute; color: var(--white); white-space: nowrap; }
  .feature-label--leader { left: 210px; top: 338px; font-size: 25px; font-weight: 600; letter-spacing: 0.4px; }
  .feature-label--strategy {
    left: 560px; top: 507px; width: 426px; text-align: center;
    font-size: 25px; font-weight: 700; font-style: italic; line-height: 34px; letter-spacing: 0.5px;
  }
  .feature-label--training { left: 270px; top: 642px; font-size: 44px; font-weight: 700; letter-spacing: 1.5px; }
  .feature-label--writing { left: 560px; top: 748px; width: 304px; text-align: center; font-size: 48px; font-weight: 400; }

  .site-footer { position: absolute; top: 923px; left: 0; width: 1200px; text-align: center; color: var(--orange); font-size: 17px; line-height: 30px; }
  .site-footer a { color: var(--orange); text-decoration: none; }
</style>
</head>
<body>
  <a class="member-link" href="#">Member Log In / Sign up Free</a>

  <header class="brand">
    <span class="brand-mark"></span>
    <span class="brand-name">THE CRUX</span>
  </header>

  <div class="rule rule--top"></div>
  <nav class="main-nav">
    <a href="#" style="left:129px">What’s The Crux ?</a>
    <a href="#" style="left:360px">What We Do</a>
    <a href="#" style="left:536px">Why The Crux ?</a>
    <a href="#" style="left:749px">Did You Know...</a>
    <a href="#" style="left:940px">Contact Us</a>
  </nav>
  <div class="rule rule--nav"></div>

  <svg class="feature-art" width="1200" height="1000" viewBox="0 0 1200 1000" aria-hidden="false">
    <defs>
      <radialGradient id="icon-fill" cx="35%" cy="30%" r="75%">
        <stop offset="0" stop-color="var(--purple-light)"/>
        <stop offset="0.6" stop-color="var(--purple)"/>
        <stop offset="1" stop-color="var(--purple-deep)"/>
      </radialGradient>
    </defs>
    <g fill="var(--purple)" stroke="var(--gold)" stroke-width="6">
      <ellipse cx="435" cy="357" rx="370" ry="84"/>
      <ellipse cx="810" cy="540" rx="326" ry="92"/>
      <ellipse cx="310" cy="675" rx="223" ry="74"/>
      <ellipse cx="740" cy="785" rx="258" ry="82"/>
    </g>
    <g stroke="var(--gold)" stroke-width="5" fill="url(#icon-fill)">
      <circle cx="130" cy="357" r="67" role="img" aria-label="Lightbulb icon for thought leader development"/>
      <circle cx="1050" cy="543" r="93" role="img" aria-label="Compass icon for marketing strategy"/>
      <circle cx="160" cy="675" r="96" role="img" aria-label="Key icon for training"/>
      <circle cx="920" cy="785" r="74" role="img" aria-label="Cogs icon for writing"/>
    </g>
    <g fill="none" stroke="var(--purple-deep)" stroke-width="2">
      <circle cx="130" cy="357" r="70"/>
      <circle cx="1050" cy="543" r="96"/>
      <circle cx="160" cy="675" r="99"/>
      <circle cx="920" cy="785" r="77"/>
    </g>
  </svg>

  <a class="feature-label feature-label--leader" href="#">Check Out The Tough Leader Devlopment</a>
  <a class="feature-label feature-label--strategy" href="#">Benefit Now With Our<br>Marketing Strategy</a>
  <a class="feature-label feature-label--training" href="#">Training!</a>
  <a class="feature-label feature-label--writing" href="#">Writing...</a>

  <div class="rule rule--foot"></div>
  <footer class="site-footer">
    <div><a href="#">Home</a> | <a href="#">Terms And Conditions</a> | <a href="#">Contact Us</a></div>
    <div>©2013 Company Name All Rights Reserved | <a href="#">Privacy Policy</a></div>
  </footer>
</body>
</html>
```